Flyer-Design für IT Firma
Zielgruppe
Wir sind eine IT Firma aus München und möchten unsere Dienstleistung vermarkten. Unsere Zielgruppe sind hauptsächlich Endkunden und kleinere Firmen.
Aufgabenstellung
Ich habe mal einen Flyer gesehen der ebenfalls IT Dienstleistung beworben hat und in Kachelform mit kleinen Icons zu den Dienstleistungen aufgebaut war. War ganz schön aber ist nicht zwingend. Gerne lassen wir uns von neuen Vorschlägen überraschen.
Format war A6 Doppelseitig angedacht. Falls sich ein anderes Format besser eignet sind wir auch dafür offen.
Den Inhalt habe ich als Word Datei hoch geladen.
Das Logo habe ich leider nicht als EI oder APS Datei, und somit auch nur als Word Datei hoch geladen. Jedes Element ist aber einzeln bearbeitbar. Falls in Verbindung mit dem Flyer Design eine leichte Modernisierung des Logos notwendig ist, wäre das kein Problem.

```html
<!DOCTYPE html>
<html lang="de">
<head>
<meta charset="utf-8">
<title>Flyer Vorderseite – Lokaler Computer Service München</title>
<link rel="stylesheet" href="https://fonts.googleapis.com/css2?family=Arimo:wght@700&family=Roboto+Condensed:ital,wght@0,400;1,400&family=Great+Vibes&family=Ubuntu:wght@400&display=swap">
<style>
  :root {
    --stage: #2b2b2b;
    --ink-dark: #1e1e1e;
    --brand-blue: #0a72c4;
    --text-white: #ffffff;
    --text-grey: #a8a8a8;
    --text-faded: #3c3c3c;
    --art-teal: #1fb5a8;
    --art-blue: #1565e0;
    --art-deep: #0a1aa0;
  }
  * { margin: 0; padding: 0; box-sizing: border-box; }
  html, body {
    width: 896px; height: 1200px; overflow: hidden;
    background: var(--stage);
  }
  .flyer {
    position: absolute; left: 48px; top: 32px;
    width: 800px; height: 1136px; overflow: hidden;
    background: var(--ink-dark);
  }
  .flyer__art { position: absolute; inset: 0; }
  .headline {
    position: absolute; left: 51px;
    font-family: "Roboto Condensed", "Arial Narrow", sans-serif;
    font-weight: 400; font-style: normal;
    font-size: 38px; line-height: 32px; letter-spacing: -0.01em;
    color: var(--text-white); text-transform: uppercase;
  }
  .headline--offer { top: 172px; }
  .headline--service { top: 400px; }
  .headline .is-grey { color: var(--text-grey); }
  .since {
    position: absolute; left: 573px; top: 68px;
    font-family: "Roboto Condensed", "Arial Narrow", sans-serif;
    font-style: italic; font-size: 18px; color: var(--text-white);
    white-space: nowrap;
  }
  .since__script {
    font-family: "Great Vibes", cursive; font-style: normal; font-size: 26px;
  }
  .claim {
    position: absolute; left: 70px; top: 737px; width: 671px; height: 156px;
    background: var(--ink-dark);
    padding-top: 22px;
    font-family: "Roboto Condensed", "Arial Narrow", sans-serif;
    font-style: italic; font-size: 29px; line-height: 32px;
    text-align: center; color: var(--text-white);
    box-shadow: 0 6px 14px rgba(0,0,0,0.35);
  }
  .claim .is-grey { color: var(--text-grey); }
  .claim .is-faded { color: var(--text-faded); }
  .footer {
    position: absolute; left: 0; top: 982px; width: 800px; height: 154px;
    background: var(--ink-dark);
  }
  .footer__text {
    position: absolute; left: 49px; top: 36px; width: 520px;
    font-family: "Ubuntu", sans-serif; font-size: 14px; line-height: 18.5px;
    letter-spacing: 0.02em; color: var(--text-white); white-space: nowrap;
  }
  .footer__brand {
    position: absolute; left: 590px; top: 40px;
    font-family: "Arimo", Arial, sans-serif; font-weight: 700;
    font-size: 42px; line-height: 46px; letter-spacing: 0.02em;
    color: var(--text-white);
  }
</style>
</head>
<body>
<main class="flyer">
  <svg class="flyer__art" width="800" height="1136" viewBox="0 0 800 1136" xmlns="http://www.w3.org/2000/svg">
    <defs>
      <linearGradient id="heroTones" x1="0" y1="0" x2="1" y2="0">
        <stop offset="0" stop-color="#141414"/>
        <stop offset="0.4" stop-color="#2a2a2a"/>
        <stop offset="0.55" stop-color="#6b5a4e"/>
        <stop offset="0.75" stop-color="#8a8a8a"/>
        <stop offset="1" stop-color="#d6d6d6"/>
      </linearGradient>
      <linearGradient id="deskTones" x1="0" y1="0" x2="0" y2="1">
        <stop offset="0" stop-color="#d8d8d8"/>
        <stop offset="1" stop-color="#c6c6c6"/>
      </linearGradient>
      <linearGradient id="artTones" x1="0" y1="0" x2="1" y2="1">
        <stop offset="0" stop-color="var(--art-teal)"/>
        <stop offset="0.5" stop-color="var(--art-blue)"/>
        <stop offset="1" stop-color="var(--art-deep)"/>
      </linearGradient>
    </defs>

    <rect role="img" aria-label="Foto: Hand zeigt nach vorn, im Hintergrund eine Person im weißen Kittel" x="0" y="0" width="800" height="564" fill="url(#heroTones)"/>
    <rect x="0" y="0" width="543" height="564" fill="var(--ink-dark)" opacity="0.55"/>
    <rect role="img" aria-label="Foto: Tischkante" x="0" y="564" width="800" height="61" fill="#7a7a7a"/>
    <rect role="img" aria-label="Schwarzweißfoto: Schreibtisch mit Laptop, Brille, Stift und Stethoskop" x="0" y="625" width="800" height="359" fill="url(#deskTones)"/>

    <polygon class="band band--blue" points="0,158 273,87 273,268 0,344" fill="var(--brand-blue)"/>
    <polygon class="band band--dark" points="0,390 273,318 273,498 0,574" fill="var(--ink-dark)"/>

    <rect role="img" aria-label="Illustration: Haus mit Glühbirne über der zeigenden Hand" x="273" y="101" width="507" height="514" fill="url(#artTones)" opacity="0.9"/>

    <polygon class="band band--badge" points="543,0 800,0 800,93 543,181" fill="var(--ink-dark)"/>
  </svg>

  <h1 class="headline headline--offer">Beratung<br><span class="is-grey">Computer</span><br>Verkauf</h1>
  <h2 class="headline headline--service">Lokaler<br><span class="is-grey">Computer</span><br>Service</h2>

  <p class="since">seit über 20 <span class="since__script">Jahren</span></p>

  <blockquote class="claim">
    „Ihr <span class="is-grey">zuverlässiger</span> Partner <span class="is-grey">seit über</span> 20 Jahren <span class="is-grey">für</span><br>
    Hard- &amp; Software Produkte <span class="is-grey">und</span> <span class="is-faded">IT &amp; EDV</span><br>
    <span class="is-grey">Dienstleistung</span> in München “
  </blockquote>

  <footer class="footer">
    <p class="footer__text">Sie bekommen eine kompetente Beratung zu allen Produkten<br>gängiger IT-Hersteller und bei der geplanten Einrichtung von<br>Heim- &amp; Firmennetzwerken.</p>
    <p class="footer__brand">NORVEK</p>
  </footer>
</main>
</body>
</html>
```